Corvelle Matchmaking - Innovative AI-based Online Dating App

Hello, I am creating a new online dating app that subsumes the personalization and compatibility analysis of human matchmaking, but is combined with the convenience of modern dating apps such as brisket. The app is called Corvelle.

There is a lot of pain and fatigue in modern online dating. Corvelle uses a concise but effective questionnaire that is combined with cutting-edge AI, social psychology research, and psycholinguistic modelling to effectively and conveniently find dating matches with real compatibility - as opposed to any major app on the market. A personalized introduction for every user is generated everyday to introduce you to a new potential match - this introduction is totally unique and will never be seen before or again. The introduction is intertwined with the user’s images to create an attractive “newsletter” feel.

"Corvelle" is Italian for lagoon, which is "a shallow body of water protected from a larger body of water (usually the ocean) by sandbars, barrier islands, or coral reefs." Lagoons are beautiful, tropical, lush watery paradises - as I see it. This is meant to be the inspiration for the feel, color scheme and design of the app.

To that end, I have included concept images of lagoons to evoke the feeling of a paradise getaway where one may meet their soulmate. This is the feeling I would like to convey with the minimalist app design this product needs to compete.

I have included screenshots of the current app UI. There is a screen for
1) potential matches and incoming likes (just like Brisket) with a logo at the top. There are “Like”, “Dislike”, “Super Like”, and “Super Dislike” buttons that float over the screen as it scrolls. These button shape/colors likely need to change to match the rest of the design
2) Overview of message threads with each match
3) View of message threads
4) Settings page

I would like
1) the logo/header image to be redone (as well as the like/dislike/super like/super dislike buttons to be redone to match the new design)
2) icons for the 4 pages in the bottom navigation bar to be redone
3) color scheme to be optimized and evoking of the desired paradise but professional feeling of a hyper-intelligent (but also empathetic) matchmaker
4) design for the settings screen (to look professional and competitive with other dating apps)

The color scheme /layout/spacing/font(s) for the bubbles on the screen where new potential matches are introduced is the most important part of the design I’m looking for. It’s currently a stack of rounded rectangles basically, but I’m open to all ideas to make this app look as professional as possible while conveying the desired elegance, empathy, and uniqueness of the brand.

Thank you!

Target Market(s)

Single men and women ages 20 - 45

Industry/Entity Type

Online dating / Matchmaking

Requirements
Must have
• For the main screen where new users are being introduced (i.e. the "swipe" page on most dating apps) - some amount of matchmaking introductory text MUST be shown above the user's first profile picture, as indicated in the current screenshots.
Nice to have
• Re-designs of the top "Corvelle" logo/emblem would be nice. If changing the logo, some emblem or graphic in addition to just the text of "Corvelle" would be nice. (Like the way "plumway" has its red flame emblem)
Should not have
• The main "swipe" page should not look identical to other dating apps in the sense of being >90% just a user's first dating profile image. The competitive edge to this app is the user-to-user specific matchmaking introductory text, so some of that must be visible before a user scrolls down for further profile information.

```html
<!DOCTYPE html>
<html lang="en">
<head>
<meta charset="utf-8">
<title>Corvelle Matchmaking – App Design Board</title>
<link rel="stylesheet" href="https://fonts.googleapis.com/css2?family=Poppins:wght@400;500;600;700&display=swap">
<style>
:root{
  --green:#22b573;
  --green-2:#2ec27e;
  --teal:#1a9c8c;
  --blue:#1553d6;
  --blue-2:#1e6fe0;
  --ink:#1d1f24;
  --muted:#8a9099;
  --line:#e7eaef;
  --field:#eef0f3;
  --chip:#1e7fe6;
  --red:#ee2a63;
  --grad:linear-gradient(90deg,var(--green) 0%,var(--teal) 45%,var(--blue) 100%);
}
*{box-sizing:border-box;margin:0;padding:0}
html,body{width:1200px;height:3002px;overflow:hidden}
body{font-family:"Poppins",sans-serif;color:var(--ink);background:linear-gradient(120deg,var(--green),var(--blue));position:relative}
.board{position:absolute;left:14px;top:14px;width:1172px;height:2974px;background:#fff;border-radius:18px}
.abs{position:absolute}

/* brand + tags */
.brand-lockup{position:absolute;left:820px;top:150px;display:flex;align-items:center;gap:14px}
.brand-lockup .mark{width:26px;height:26px;border-radius:50%;background:var(--blue-2)}
.brand-lockup .word{font-size:62px;font-weight:500;letter-spacing:6px;color:var(--teal);line-height:1}
.tag{position:absolute;border:2px solid var(--teal);border-radius:7px;font-size:17px;font-weight:600;display:flex;align-items:center;justify-content:center;height:45px;color:var(--ink)}

/* vertical labels */
.vlabel{position:absolute;width:20px;height:598px;writing-mode:vertical-rl;transform:rotate(180deg);font-size:12px;font-weight:700;letter-spacing:9px;color:var(--green);text-align:start;white-space:nowrap}

/* screen */
.screen{position:absolute;width:282px;height:598px;border-radius:34px;overflow:hidden;background:#fff;box-shadow:0 0 0 1px var(--line),0 10px 30px rgba(20,60,120,.12)}
.mini{transform:scale(.7);transform-origin:0 0}
.status{position:absolute;top:14px;left:26px;right:22px;display:flex;justify-content:space-between;font-size:11px;font-weight:600;z-index:3}
.status.light{color:#fff}
.status .sys{display:flex;gap:4px;align-items:center}
.status .sys i{display:block;background:currentColor;border-radius:2px}
.homebar{position:absolute;bottom:10px;left:50%;width:100px;height:4px;margin-left:-50px;border-radius:3px;background:#fff;z-index:4}
.homebar.dark{background:var(--ink)}

.photo{position:absolute;display:block}
.photo-stage{background:linear-gradient(165deg,#6d1b1f 0%,#3b2a22 35%,#2f6a45 70%,#1c3b2a 100%)}
.photo-lagoon{background:linear-gradient(180deg,#2fb59a 0%,#1f9aa8 40%,#1a78c2 75%,#1557c9 100%)}
.photo-beach{background:linear-gradient(160deg,#7fb6d6,#d9c3a3 60%,#b58f6b)}
.photo-field{background:linear-gradient(180deg,#a8c4dc,#e2ddd4 55%,#9eaa86)}
.photo-portrait{background:linear-gradient(160deg,#c9a07f,#8a5e45)}
.photo-coast{background:linear-gradient(160deg,#6fa6d9,#b59376 60%,#6b5846)}

.app-brand{position:absolute;display:flex;align-items:center;gap:5px;font-size:13px;font-weight:500;color:#fff;letter-spacing:1.5px}
.app-brand .mark{width:7px;height:7px;border-radius:50%;background:#fff}

.dots-btn{position:absolute;width:22px;height:22px;border-radius:50%;background:#fff;display:flex;align-items:center;justify-content:center}

.profile-card{position:absolute;left:18px;right:24px;background:#fff;border-radius:12px;box-shadow:0 6px 18px rgba(0,0,0,.12);padding:12px 12px}
.profile-card .name{font-size:16px;font-weight:600}
.profile-card .name small{font-size:12px;font-weight:500;margin-left:4px}
.profile-card .role{font-size:9.5px;color:var(--muted);margin-top:1px}
.distance{position:absolute;right:10px;top:12px;font-size:8px;color:var(--muted);border:1px solid var(--line);border-radius:10px;padding:2px 7px;display:flex;gap:3px;align-items:center}
.chips{display:flex;gap:6px;flex-wrap:wrap;margin-top:11px}
.chip{display:inline-flex;align-items:center;gap:4px;background:var(--chip);color:#fff;font-size:7.5px;border-radius:10px;padding:3px 8px 3px 4px}
.chip i{display:block;width:9px;height:9px;border-radius:50%;background:rgba(255,255,255,.55)}

.letter{position:absolute;left:18px;right:18px;font-size:8.6px;line-height:1.82;color:#2a2d33}
.letter p{margin-bottom:12px}
.letter .hl{color:var(--green);font-weight:500}
.fade{-webkit-mask-image:linear-gradient(180deg,#000 40%,transparent);mask-image:linear-gradient(180deg,#000 40%,transparent)}

.actions{position:absolute;left:0;right:0;height:50px;z-index:3}
.act{position:absolute;width:38px;height:38px;border-radius:50%;background:#fff;box-shadow:0 4px 12px rgba(0,0,0,.16);display:flex;align-items:center;justify-content:center;transform:translate(-50%,-50%);top:25px}
.act.big{width:48px;height:48px}

.nav{position:absolute;left:0;bottom:0;width:282px;height:90px;z-index:2}

/* sign in */
.sheet{position:absolute;left:0;right:0;top:178px;bottom:0;background:#fff;border-radius:22px 22px 0 0}
.field{position:absolute;left:22px;right:22px;height:34px;background:var(--field);border-radius:6px;display:flex;align-items:center;gap:10px;padding-left:12px;font-size:9.5px;color:#a2a7ae}
.btn-grad{position:absolute;left:22px;right:22px;height:36px;border-radius:18px;background:var(--grad);color:#fff;font-size:11px;font-weight:600;display:flex;align-items:center;justify-content:center}
.btn-out{position:absolute;height:36px;border-radius:18px;font-size:12px;font-weight:600;display:flex;align-items:center;justify-content:center}

/* info card */
.info-card{position:absolute;left:20px;right:20px;background:#fff;border-radius:10px;box-shadow:0 4px 18px rgba(0,0,0,.08);padding:14px 14px}
.info-card h4{font-size:10.5px;font-weight:500}
.facts{background:#f3f5f8;border-radius:6px;display:flex;justify-content:space-around;padding:8px 6px;margin-top:14px}
.fact{text-align:center}
.fact span{display:block;font-size:6px;color:var(--muted);letter-spacing:.5px}
.fact b{font-size:8.5px;font-weight:500;display:flex;gap:5px;align-items:center;justify-content:center;margin-top:4px}
.row{display:flex;justify-content:space-between;font-size:8.5px;border-bottom:1px solid var(--line);padding:9px 0 8px}
.row span{color:var(--muted)}

/* messages */
.title{position:absolute;left:20px;font-size:19px;font-weight:600}
.search{position:absolute;left:16px;right:16px;height:28px;background:var(--field);border-radius:7px;display:flex;align-items:center;gap:7px;padding-left:12px;font-size:9px;color:var(--muted)}
.thread{position:absolute;left:10px;right:10px;height:56px;display:flex;align-items:center;padding:0 10px;gap:10px;border-radius:8px}
.thread.active{background:var(--grad);color:#fff}
.avatar{width:38px;height:38px;border-radius:50%;flex:none;background:linear-gradient(160deg,#d7b194,#7b5440)}
.thread .meta{flex:1}
.thread .who{font-size:10px;font-weight:600}
.thread .who.g{color:var(--green)}
.thread .snip{font-size:8px;color:var(--muted);margin-top:2px}
.thread .snip.g{color:var(--green)}
.thread.active .snip{color:#fff}
.thread .side{text-align:right;font-size:7px;color:var(--muted)}
.thread.active .side{color:#fff}
.thread .side i{display:block;width:7px;height:7px;border-radius:50%;background:var(--green);margin:6px 0 0 auto}

/* chat */
.bubble{position:absolute;font-size:9px;padding:7px 10px;border-radius:8px;white-space:nowrap}
.bubble.out{right:16px;background:var(--green);color:#fff}
.bubble.in{left:48px;background:#eef0f3;color:#2a2d33}
.bubble-av{position:absolute;left:16px;width:24px;height:24px;border-radius:50%;background:linear-gradient(160deg,#d7b194,#7b5440)}

/* profile */
.pcard{position:absolute;left:16px;right:16px;top:79px;height:211px;border-radius:14px;background:linear-gradient(135deg,var(--green),var(--teal) 45%,var(--blue))}
.stats{position:absolute;left:12px;right:12px;top:114px;height:40px;border-radius:8px;background:rgba(10,60,140,.35);display:flex;justify-content:space-around;align-items:center;color:#fff;text-align:center}
.stats b{display:block;font-size:12px;font-weight:500}
.stats span{font-size:5.5px;letter-spacing:.5px;opacity:.85}
.pbtn{position:absolute;top:168px;height:30px;border-radius:15px;font-size:9px;font-weight:500;display:flex;align-items:center;justify-content:center;gap:6px}
.panel{position:absolute;left:16px;right:16px;background:#fff;border-radius:10px;box-shadow:0 4px 18px rgba(0,0,0,.08);padding:12px 14px}
.panel h4{font-size:10px;font-weight:500;display:flex;justify-content:space-between}
</style>
</head>
<body>
<svg width="0" height="0" style="position:absolute" aria-hidden="true">
  <defs>
    <linearGradient id="g-brand" x1="0" x2="1" y1="0" y2="0"><stop offset="0" stop-color="#22b573"/><stop offset=".45" stop-color="#1a9c8c"/><stop offset="1" stop-color="#1553d6"/></linearGradient>
    <symbol id="ic-home" viewBox="0 0 24 24"><path d="M3 11 12 3l9 8v9a1 1 0 0 1-1 1h-5v-6H9v6H4a1 1 0 0 1-1-1z" fill="currentColor"/></symbol>
    <symbol id="ic-search" viewBox="0 0 24 24"><circle cx="11" cy="11" r="7" fill="none" stroke="currentColor" stroke-width="3"/><path d="m16 16 5 5" stroke="currentColor" stroke-width="3" stroke-linecap="round"/></symbol>
    <symbol id="ic-chat" viewBox="0 0 24 24"><path d="M4 4h16a1 1 0 0 1 1 1v11a1 1 0 0 1-1 1H9l-5 4v-4H4a1 1 0 0 1-1-1V5a1 1 0 0 1 1-1z" fill="currentColor"/><circle cx="8" cy="10.5" r="1.4" fill="#1a9c8c"/><circle cx="12" cy="10.5" r="1.4" fill="#1a9c8c"/><circle cx="16" cy="10.5" r="1.4" fill="#1a9c8c"/></symbol>
    <symbol id="ic-user" viewBox="0 0 24 24"><circle cx="12" cy="12" r="10" fill="currentColor"/><circle cx="12" cy="10" r="3.3" fill="#1553d6"/><path d="M6 18c1.5-3 3.5-4 6-4s4.5 1 6 4" fill="#1553d6"/></symbol>
    <symbol id="ic-broken" viewBox="0 0 24 24"><path d="M12 21 3.5 12.5A5 5 0 0 1 11 6l1 1-2 4 3 2-2 4 2-4-3-2 2-4 1-1a5 5 0 0 1 7.5 6.5z" fill="#1b5fd1"/></symbol>
    <symbol id="ic-x" viewBox="0 0 24 24"><path d="M5 5l14 14M19 5 5 19" stroke="#ee2a63" stroke-width="2.6" stroke-linecap="round"/></symbol>
    <symbol id="ic-heart" viewBox="0 0 24 24"><path d="M12 21 3.5 12.5A5 5 0 0 1 12 6a5 5 0 0 1 8.5 6.5z" fill="url(#g-brand)"/></symbol>
    <symbol id="ic-star" viewBox="0 0 24 24"><path d="m12 3 2.7 5.7 6.3.8-4.6 4.3 1.2 6.2L12 17l-5.6 3 1.2-6.2L3 9.5l6.3-.8z" fill="#1b5fd1"/></symbol>
    <symbol id="ic-pin" viewBox="0 0 24 24"><path d="M12 2a7 7 0 0 1 7 7c0 5-7 13-7 13S5 14 5 9a7 7 0 0 1 7-7z" fill="currentColor"/><circle cx="12" cy="9" r="2.5" fill="#fff"/></symbol>
    <symbol id="ic-edit" viewBox="0 0 24 24"><path d="M4 20l1-5L16 4l4 4L9 19z" fill="currentColor"/></symbol>
    <symbol id="ic-gear" viewBox="0 0 24 24"><circle cx="12" cy="12" r="7" fill="none" stroke="currentColor" stroke-width="4" stroke-dasharray="3.5 2"/><circle cx="12" cy="12" r="4.5" fill="none" stroke="currentColor" stroke-width="2.5"/></symbol>
    <symbol id="ic-send" viewBox="0 0 24 24"><path d="M3 20 21 12 3 4l2 7 9 1-9 1z" fill="#fff"/></symbol>
    <symbol id="ic-plus" viewBox="0 0 24 24"><circle cx="12" cy="12" r="10" fill="#1553d6"/><path d="M12 7v10M7 12h10" stroke="#fff" stroke-width="2.4" stroke-linecap="round"/></symbol>
    <symbol id="ic-back" viewBox="0 0 24 24"><path d="M20 12H5m6-7-7 7 7 7" fill="none" stroke="#22b573" stroke-width="2.4" stroke-linecap="round" stroke-linejoin="round"/></symbol>
    <symbol id="ic-dots" viewBox="0 0 24 24"><circle cx="12" cy="5" r="2" fill="currentColor"/><circle cx="12" cy="12" r="2" fill="currentColor"/><circle cx="12" cy="19" r="2" fill="currentColor"/></symbol>
    <symbol id="ic-mail" viewBox="0 0 24 24"><rect x="3" y="5" width="18" height="14" rx="2" fill="#8a9099"/><path d="m3 7 9 6 9-6" fill="none" stroke="#eef0f3" stroke-width="1.8"/></symbol>
    <symbol id="ic-lock" viewBox="0 0 24 24"><rect x="5" y="10" width="14" height="11" rx="2" fill="#8a9099"/><path d="M8 10V7a4 4 0 0 1 8 0v3" fill="none" stroke="#8a9099" stroke-width="2.4"/></symbol>
    <symbol id="ic-cake" viewBox="0 0 24 24"><rect x="4" y="12" width="16" height="9" rx="1" fill="currentColor"/><rect x="11" y="6" width="2" height="6" fill="currentColor"/></symbol>
    <symbol id="ic-female" viewBox="0 0 24 24"><circle cx="12" cy="9" r="5" fill="none" stroke="currentColor" stroke-width="2.4"/><path d="M12 14v8M8.5 18.5h7" stroke="currentColor" stroke-width="2.4"/></symbol>
    <symbol id="ic-male" viewBox="0 0 24 24"><circle cx="10" cy="14" r="5.5" fill="none" stroke="currentColor" stroke-width="2.4"/><path d="M14 10l6-6m-5 0h5v5" fill="none" stroke="currentColor" stroke-width="2.4"/></symbol>
    <symbol id="ic-photo" viewBox="0 0 24 24"><rect x="3" y="5" width="18" height="14" rx="2" fill="currentColor"/><circle cx="9" cy="10" r="2" fill="#fff"/><path d="m5 17 5-4 3 2 3-3 4 5z" fill="#fff"/></symbol>
    <symbol id="nav-bar" viewBox="0 0 282 90">
      <path d="M0 26 C70 4 190 -2 282 14 V90 H0Z" fill="url(#g-brand)"/>
    </symbol>
  </defs>
</svg>

<div class="board">

  <!-- ============ presentation header ============ -->
  <div class="brand-lockup" style="left:806px;top:138px"><span class="mark"></span><span class="word">CORVELLE</span></div>

  <div class="tag" style="left:810px;top:285px;width:121px">App design</div>
  <div class="tag" style="left:955px;top:285px;width:104px">Flat style</div>
  <div class="tag" style="left:810px;top:354px;width:93px">Modern</div>
  <div class="tag" style="left:927px;top:354px;width:99px">Clean UI</div>
  <div class="tag" style="left:810px;top:424px;width:166px">Rounded corners</div>
  <div class="tag" style="left:810px;top:493px;width:88px">Playful</div>

  <!-- header mini screens -->
  <div class="screen mini" style="left:96px;top:86px">
    <span class="photo photo-stage" role="img" aria-label="Profile photo of Marisol performing on stage" style="left:0;top:0;width:282px;height:335px;border-radius:0 0 30px 30px"></span>
    <div class="status light"><span>9:41</span><span class="sys"><i style="width:12px;height:7px"></i><i style="width:16px;height:8px"></i></span></div>
    <div class="app-brand" style="left:18px;top:36px"><span class="mark"></span>Corvelle</div>
    <div class="dots-btn" style="right:16px;top:36px"><svg width="12" height="12" style="color:#333"><use href="#ic-dots"/></svg></div>
    <div class="profile-card" style="top:268px">
      <div class="name">Marisol<small>34</small></div>
      <div class="role">Singer/Songwriter</div>
      <div class="distance"><svg width="8" height="8"><use href="#ic-pin"/></svg>1 km away</div>
      <div class="chips"><span class="chip"><i></i>Music</span><span class="chip"><i></i>Singing</span><span class="chip"><i></i>Books</span></div>
    </div>
    <div class="letter fade" style="top:385px;height:60px"><p>Dear Pritish,</p><p>Allow me to introduce you to <span class="hl">Marisol</span>, a captivating woman who possesses an enchanting blend of</p></div>
    <div class="actions" style="top:464px">
      <div class="act" style="left:56px"><svg width="16" height="16"><use href="#ic-broken"/></svg></div>
      <div class="act big" style="left:110px"><svg width="18" height="18"><use href="#ic-x"/></svg></div>
      <div class="act big" style="left:171px"><svg width="24" height="24"><use href="#ic-heart"/></svg></div>
      <div class="act" style="left:225px"><svg width="14" height="14"><use href="#ic-star"/></svg></div>
    </div>
    <svg class="nav" viewBox="0 0 282 90" style="top:508px"><use href="#nav-bar"/><g color="#fff"><use href="#ic-home" x="30" y="29" width="16" height="16"/><use href="#ic-search" x="99" y="29" width="16" height="16"/><use href="#ic-chat" x="166" y="29" width="16" height="16" opacity=".6"/><use href="#ic-user" x="234" y="29" width="16" height="16" opacity=".6"/></g></svg>
    <div class="homebar"></div>
  </div>

  <div class="screen mini" style="left:306px;top:246px">
    <span class="photo photo-stage" role="img" aria-label="Top edge of Marisol's profile photo" style="left:0;top:0;width:282px;height:70px;border-radius:0 0 30px 30px"></span>
    <div class="status light"><span>9:41</span><span class="sys"><i style="width:12px;height:7px"></i><i style="width:16px;height:8px"></i></span></div>
    <div class="profile-card" style="top:34px">
      <div class="name">Marisol<small>34</small></div>
      <div class="role">Singer/Songwriter</div>
      <div class="distance"><svg width="8" height="8"><use href="#ic-pin"/></svg>1 km away</div>
      <div class="chips"><span class="chip"><i></i>Music</span><span class="chip"><i></i>Singing</span><span class="chip"><i></i>Books</span></div>
    </div>
    <div class="letter" style="top:156px"><p>Dear Pritish,</p><p>Allow me to introduce you to <span class="hl">Marisol</span>, a captivating woman who possesses an enchanting blend of qualities that perfectly align with what you seek in a partner. Her shared interest in creativity is just the beginning of the profound connection you could share. Marisol's passion for games, documentaries, music, and writing mirrors your own, promising endless hours of intellectual stimulation and shared experiences.</p><p>But it is her adventurous spirit and independent nature that truly sets Marisol apart. She embraces life with a discerning eye, always seeking new and exciting opportunities. Her love for the beach, fashion, walking, books, swimming, and dancing reveals a zest for life that perfectly complements your own desire for exploration and discovery.</p></div>
    <span class="photo photo-beach" role="img" aria-label="Faded gallery photos" style="left:18px;top:438px;width:112px;height:80px;opacity:.35;border-radius:6px"></span>
    <span class="photo photo-field" role="img" aria-label="Faded gallery photos" style="left:142px;top:438px;width:112px;height:80px;opacity:.35;border-radius:6px"></span>
    <div class="actions" style="top:464px">
      <div class="act" style="left:56px"><svg width="16" height="16"><use href="#ic-broken"/></svg></div>
      <div class="act big" style="left:110px"><svg width="18" height="18"><use href="#ic-x"/></svg></div>
      <div class="act big" style="left:171px"><svg width="24" height="24"><use href="#ic-heart"/></svg></div>
      <div class="act" style="left:225px"><svg width="14" height="14"><use href="#ic-star"/></svg></div>
    </div>
    <svg class="nav" viewBox="0 0 282 90" style="top:508px"><use href="#nav-bar"/><g color="#fff"><use href="#ic-home" x="30" y="29" width="16" height="16" opacity=".6"/><use href="#ic-search" x="99" y="29" width="16" height="16"/><use href="#ic-chat" x="166" y="29" width="16" height="16" opacity=".6"/><use href="#ic-user" x="234" y="29" width="16" height="16" opacity=".6"/></g></svg>
    <div class="homebar"></div>
  </div>

  <div class="screen mini" style="left:516px;top:156px">
    <div class="status"><span>9:41</span><span class="sys"><i style="width:12px;height:7px"></i><i style="width:16px;height:8px"></i></span></div>
    <div class="pcard">
      <div class="stats"><div><b>740</b><span>FOLLOWING</span></div><div><b>506</b><span>FOLLOWERS</span></div><div><b>128</b><span>LIKES</span></div></div>
      <div class="pbtn" style="left:12px;width:112px;border:1px solid #fff;color:#fff"><svg width="9" height="9" color="#fff"><use href="#ic-edit"/></svg>Edit profile</div>
      <div class="pbtn" style="right:12px;width:112px;background:#fff;color:var(--blue)"><svg width="11" height="11" color="#1553d6"><use href="#ic-photo"/></svg>Add</div>
      <div class="abs" style="left:0;right:0;top:85px;text-align:center;color:#fff;font-size:15px;font-weight:600">Spencer</div>
    </div>
    <span class="photo photo-coast" role="img" aria-label="Profile photo of Spencer on a rocky coast" style="left:89px;top:46px;width:104px;height:104px;border-radius:50%;border:3px solid #fff"></span>
    <svg class="abs" style="right:20px;top:44px" width="14" height="14" color="#22b573"><use href="#ic-gear"/></svg>
    <div class="panel" style="top:306px;height:104px"><h4>Interests<svg width="10" height="10" color="#1553d6"><use href="#ic-edit"/></svg></h4>
      <div class="chips" style="margin-top:12px"><span class="chip"><i></i>Motorcycle</span><span class="chip"><i></i>Books</span><span class="chip"><i></i>Music</span><span class="chip"><i></i>Beach</span><span class="chip"><i></i>Camping</span></div></div>
    <div class="panel" style="top:429px;height:110px"><h4>More about Spencer<svg width="10" height="10" color="#1553d6"><use href="#ic-edit"/></svg></h4>
      <div class="facts"><div class="fact"><span>BIRTHDAY</span><b><svg width="9" height="9"><use href="#ic-cake"/></svg>20 Jul, 1985</b></div><div class="fact"><span>GENDER</span><b><svg width="9" height="9"><use href="#ic-male"/></svg>Male</b></div></div></div>
    <svg class="nav" viewBox="0 0 282 90" style="top:508px"><use href="#nav-bar"/><g color="#fff"><use href="#ic-home" x="30" y="29" width="16" height="16" opacity=".6"/><use href="#ic-search" x="99" y="29" width="16" height="16" opacity=".6"/><use href="#ic-chat" x="166" y="29" width="16" height="16" opacity=".6"/><use href="#ic-user" x="234" y="29" width="16" height="16"/></g></svg>
    <div class="homebar"></div>
  </div>

  <!-- ============ row 1 ============ -->
  <div class="vlabel" style="left:54px;top:874px">SPLASH SCREEN</div>
  <div class="screen" style="left:79px;top:874px">
    <span class="photo photo-lagoon" role="img" aria-label="Aerial view of a turquoise lagoon and island with a heart-shaped cloud" style="inset:0"></span>
    <div class="status light"><span>9:41</span><span class="sys"><i style="width:12px;height:7px"></i><i style="width:16px;height:8px"></i></span></div>
    <div class="app-brand" style="left:0;right:0;top:190px;justify-content:center;font-size:32px;letter-spacing:4px;gap:10px"><span class="mark" style="width:12px;height:12px"></span>Corvelle</div>
    <div class="btn-out" style="left:24px;top:505px;width:108px;border:1.5px solid #fff;color:#fff">Sign Up</div>
    <div class="btn-out" style="left:148px;top:505px;width:108px;background:#fff;color:var(--green)">Sign in</div>
    <div class="homebar"></div>
  </div>

  <div class="vlabel" style="left:423px;top:874px">SIGN IN SCREEN</div>
  <div class="screen" style="left:448px;top:874px">
    <span class="photo photo-lagoon" role="img" aria-label="Lagoon scene with a heart-shaped cloud" style="left:0;top:0;right:0;height:200px"></span>
    <div class="status light"><span>9:41</span><span class="sys"><i style="width:12px;height:7px"></i><i style="width:16px;height:8px"></i></span></div>
    <div class="sheet">
      <div class="app-brand" style="left:0;right:0;top:40px;justify-content:center;color:var(--blue-2);font-size:24px;letter-spacing:3px;gap:8px"><span class="mark" style="background:var(--green);width:9px;height:9px"></span>Corvelle</div>
      <div class="abs" style="left:22px;top:112px;font-size:15px;font-weight:600">Sign in</div>
      <div class="field" style="top:154px"><svg width="12" height="12"><use href="#ic-mail"/></svg>email address</div>
      <div class="field" style="top:198px"><svg width="12" height="12"><use href="#ic-lock"/></svg>password</div>
      <div class="abs" style="left:0;right:0;top:247px;text-align:center;font-size:10.5px;font-weight:600;color:var(--green)">Forgot password?</div>
      <div class="btn-grad" style="top:284px">Sign in</div>
      <div class="abs" style="left:0;right:0;top:359px;text-align:center;font-size:9px;color:#5a6069">Don't have an account? &nbsp;<b style="color:var(--green);font-weight:600">SIGN UP</b></div>
    </div>
    <div class="homebar dark"></div>
  </div>

  <div class="vlabel" style="left:792px;top:874px">DISCOVER SCREEN 1 / 4</div>
  <div class="screen" style="left:817px;top:874px">
    <span class="photo photo-stage" role="img" aria-label="Profile photo of Marisol performing on stage" style="left:0;top:0;width:282px;height:335px;border-radius:0 0 30px 30px"></span>
    <div class="status light"><span>9:41</span><span class="sys"><i style="width:12px;height:7px"></i><i style="width:16px;height:8px"></i></span></div>
    <div class="app-brand" style="left:18px;top:36px"><span class="mark"></span>Corvelle</div>
    <div class="dots-btn" style="right:16px;top:36px"><svg width="12" height="12" style="color:#333"><use href="#ic-dots"/></svg></div>
    <div class="profile-card" style="top:268px">
      <div class="name">Marisol<small>34</small></div>
      <div class="role">Singer/Songwriter</div>
      <div class="distance"><svg width="8" height="8"><use href="#ic-pin"/></svg>1 km away</div>
      <div class="chips"><span class="chip"><i></i>Music</span><span class="chip"><i></i>Singing</span><span class="chip"><i></i>Books</span></div>
    </div>
    <div class="letter fade" style="top:385px;height:60px"><p>Dear Pritish,</p><p>Allow me to introduce you to <span class="hl">Marisol</span>, a captivating woman who possesses an enchanting blend of</p></div>
    <div class="actions" style="top:464px">
      <div class="act" style="left:56px"><svg width="16" height="16"><use href="#ic-broken"/></svg></div>
      <div class="act big" style="left:110px"><svg width="18" height="18"><use href="#ic-x"/></svg></div>
      <div class="act big" style="left:171px"><svg width="24" height="24"><use href="#ic-heart"/></svg></div>
      <div class="act" style="left:225px"><svg width="14" height="14"><use href="#ic-star"/></svg></div>
    </div>
    <svg class="nav" viewBox="0 0 282 90" style="top:508px"><use href="#nav-bar"/><g color="#fff"><use href="#ic-home" x="30" y="29" width="16" height="16" opacity=".6"/><use href="#ic-search" x="99" y="29" width="16" height="16"/><use href="#ic-chat" x="166" y="29" width="16" height="16" opacity=".6"/><use href="#ic-user" x="234" y="29" width="16" height="16" opacity=".6"/></g></svg>
    <div class="homebar"></div>
  </div>

  <!-- ============ row 2 ============ -->
  <div class="vlabel" style="left:54px;top:1551px">DISCOVER SCREEN 2 / 4</div>
  <div class="screen" style="left:79px;top:1551px">
    <span class="photo photo-stage" role="img" aria-label="Top edge of Marisol's profile photo" style="left:0;top:0;width:282px;height:70px;border-radius:0 0 30px 30px"></span>
    <div class="status light"><span>9:41</span><span class="sys"><i style="width:12px;height:7px"></i><i style="width:16px;height:8px"></i></span></div>
    <div class="profile-card" style="top:34px">
      <div class="name">Marisol<small>34</small></div>
      <div class="role">Singer/Songwriter</div>
      <div class="distance"><svg width="8" height="8"><use href="#ic-pin"/></svg>1 km away</div>
      <div class="chips"><span class="chip"><i></i>Music</span><span class="chip"><i></i>Singing</span><span class="chip"><i></i>Books</span></div>
    </div>
    <div class="letter" style="top:156px"><p>Dear Pritish,</p><p>Allow me to introduce you to <span class="hl">Marisol</span>, a captivating woman who possesses an enchanting blend of qualities that perfectly align with what you seek in a partner. Her shared interest in creativity is just the beginning of the profound connection you could share. Marisol's passion for games, documentaries, music, and writing mirrors your own, promising endless hours of intellectual stimulation and shared experiences.</p><p>But it is her adventurous spirit and independent nature that truly sets Marisol apart. She embraces life with a discerning eye, always seeking new and exciting opportunities. Her love for the beach, fashion, walking, books, swimming, and dancing reveals a zest for life that perfectly complements your own desire for exploration and discovery.</p></div>
    <span class="photo photo-beach" role="img" aria-label="Faded gallery photos" style="left:18px;top:438px;width:112px;height:80px;opacity:.35;border-radius:6px"></span>
    <span class="photo photo-field" role="img" aria-label="Faded gallery photos" style="left:142px;top:438px;width:112px;height:80px;opacity:.35;border-radius:6px"></span>
    <div class="actions" style="top:464px">
      <div class="act" style="left:56px"><svg width="16" height="16"><use href="#ic-broken"/></svg></div>
      <div class="act big" style="left:110px"><svg width="18" height="18"><use href="#ic-x"/></svg></div>
      <div class="act big" style="left:171px"><svg width="24" height="24"><use href="#ic-heart"/></svg></div>
      <div class="act" style="left:225px"><svg width="14" height="14"><use href="#ic-star"/></svg></div>
    </div>
    <svg class="nav" viewBox="0 0 282 90" style="top:508px"><use href="#nav-bar"/><g color="#fff"><use href="#ic-home" x="30" y="29" width="16" height="16" opacity=".6"/><use href="#ic-search" x="99" y="29" width="16" height="16"/><use href="#ic-chat" x="166" y="29" width="16" height="16" opacity=".6"/><use href="#ic-user" x="234" y="29" width="16" height="16" opacity=".6"/></g></svg>
    <div class="homebar"></div>
  </div>

  <div class="vlabel" style="left:423px;top:1551px">DISCOVER SCREEN 3 / 4</div>
  <div class="screen" style="left:448px;top:1551px">
    <div class="letter" style="top:10px">exploration and discovery.</div>
    <span class="photo photo-beach" role="img" aria-label="Photo of Marisol lying on the beach" style="left:20px;top:42px;width:112px;height:116px;border-radius:4px"></span>
    <span class="photo photo-field" role="img" aria-label="Photo of Marisol standing in a field" style="left:143px;top:42px;width:112px;height:116px;border-radius:4px"></span>
    <div class="letter" style="top:176px"><p>Beyond her shared interests, Marisol's self-identification as creative, independent, and discerning resonates deeply with your own values. Her vibrant personality and unwavering sense of self make her an intriguing and captivating individual, one who possesses the potential to ignite a passionate and fulfilling romance.</p><p>In Marisol, you may find a kindred spirit, a partner who not only shares your interests but also complements your desires for adventure and creativity. I encourage you to explore the possibilities that lie within this promising connection.</p><p>Wishing you the best on this exciting journey of love and companionship.</p></div>
    <div class="letter fade" style="top:442px;color:#b7bcc3"><p>Marisol Ayala</p><p>Warm regards</p></div>
    <div class="actions" style="top:464px">
      <div class="act" style="left:56px"><svg width="16" height="16"><use href="#ic-broken"/></svg></div>
      <div class="act big" style="left:110px"><svg width="18" height="18"><use href="#ic-x"/></svg></div>
      <div class="act big" style="left:171px"><svg width="24" height="24"><use href="#ic-heart"/></svg></div>
      <div class="act" style="left:225px"><svg width="14" height="14"><use href="#ic-star"/></svg></div>
    </div>
    <svg class="nav" viewBox="0 0 282 90" style="top:508px"><use href="#nav-bar"/><g color="#fff"><use href="#ic-home" x="30" y="29" width="16" height="16" opacity=".6"/><use href="#ic-search" x="99" y="29" width="16" height="16"/><use href="#ic-chat" x="166" y="29" width="16" height="16" opacity=".6"/><use href="#ic-user" x="234" y="29" width="16" height="16" opacity=".6"/></g></svg>
    <div class="homebar"></div>
  </div>

  <div class="vlabel" style="left:792px;top:1551px">DISCOVER SCREEN 4 / 4</div>
  <div class="screen" style="left:817px;top:1551px">
    <div class="letter" style="top:6px"><p>you to explore the possibilities that lie within this promising connection.</p><p>Wishing you the best on this exciting journey of love and companionship.</p><p style="margin-bottom:6px">Warm regards,</p></div>
    <div class="abs" style="left:18px;top:128px;display:flex;align-items:center;gap:7px;font-size:8.5px"><span class="avatar" role="img" aria-label="Lester's avatar" style="width:22px;height:22px"></span>Lester</div>
    <div class="info-card" style="top:168px;height:268px">
      <h4>More about Marisol</h4>
      <div class="facts"><div class="fact"><span>BIRTHDAY</span><b><svg width="9" height="9"><use href="#ic-cake"/></svg>13 Dec, 1989</b></div><div class="fact"><span>GENDER</span><b><svg width="9" height="9"><use href="#ic-female"/></svg>Female</b></div></div>
      <div style="margin-top:14px">
        <div class="row"><span>CHILDREN</span>No child</div>
        <div class="row"><span>FAMILY GOALS</span>Open to children</div>
        <div class="row"><span>DIET</span>Omnivore</div>
        <div class="row"><span>DRINKING</span>Occasionally</div>
        <div class="row" style="border:0"><span>DRUGS</span>No</div>
      </div>
    </div>
    <div class="actions" style="top:464px">
      <div class="act" style="left:56px"><svg width="16" height="16"><use href="#ic-broken"/></svg></div>
      <div class="act big" style="left:110px"><svg width="18" height="18"><use href="#ic-x"/></svg></div>
      <div class="act big" style="left:171px"><svg width="24" height="24"><use href="#ic-heart"/></svg></div>
      <div class="act" style="left:225px"><svg width="14" height="14"><use href="#ic-star"/></svg></div>
    </div>
    <svg class="nav" viewBox="0 0 282 90" style="top:508px"><use href="#nav-bar"/><g color="#fff"><use href="#ic-home" x="30" y="29" width="16" height="16" opacity=".6"/><use href="#ic-search" x="99" y="29" width="16" height="16"/><use href="#ic-chat" x="166" y="29" width="16" height="16" opacity=".6"/><use href="#ic-user" x="234" y="29" width="16" height="16" opacity=".6"/></g></svg>
    <div class="homebar"></div>
  </div>

  <!-- ============ row 3 ============ -->
  <div class="vlabel" style="left:54px;top:2225px">MESSAGES SCREEN</div>
  <div class="screen" style="left:79px;top:2225px">
    <div class="status"><span>9:41</span><span class="sys"><i style="width:12px;height:7px"></i><i style="width:16px;height:8px"></i></span></div>
    <div class="title" style="top:40px">Messages</div>
    <div class="abs" style="right:20px;top:42px;width:26px;height:26px;border-radius:50%;background:linear-gradient(135deg,var(--green),var(--teal));display:flex;align-items:center;justify-content:center"><svg width="11" height="11" color="#fff"><use href="#ic-edit"/></svg></div>
    <div class="search" style="top:80px"><svg width="10" height="10" color="#8a9099"><use href="#ic-search"/></svg>Search</div>
    <div class="thread" style="top:119px"><span class="avatar" role="img" aria-label="Alodia's avatar"></span><div class="meta"><div class="who g">Alodia</div><div class="snip g">Awesome! See yah</div></div><div class="side">2m ago<i></i></div></div>
    <div class="thread" style="top:176px"><span class="avatar" role="img" aria-label="Megan's avatar"></span><div class="meta"><div class="who">Megan</div><div class="snip">Okay. I'll be there.</div></div><div class="side">10:16 AM</div></div>
    <div class="thread active" style="top:233px"><span class="avatar" role="img" aria-label="Alodia's avatar"></span><div class="meta"><div class="who">Alodia</div><div class="snip">It's me, hi!</div></div><div class="side">12:13 PM</div></div>
    <div class="thread" style="top:291px"><span class="avatar" role="img" aria-label="Christina's avatar"></span><div class="meta"><div class="who g">Christina</div><div class="snip g">Wow</div></div><div class="side">Jan 5<i></i></div></div>
    <div class="thread" style="top:348px"><span class="avatar" role="img" aria-label="Kimberley's avatar"></span><div class="meta"><div class="who">Kimberley</div><div class="snip">No problem</div></div><div class="side">Jan 3</div></div>
    <div class="thread" style="top:407px"><span class="avatar" role="img" aria-label="Jessica's avatar"></span><div class="meta"><div class="who g">Jessica</div><div class="snip g">That's so sweet...</div></div><div class="side">Jan 2<i></i></div></div>
    <div class="thread" style="top:465px"><span class="avatar" role="img" aria-label="Francine's avatar"></span><div class="meta"><div class="who">Francine</div><div class="snip">Happy new year!!!</div></div><div class="side">Jan 1</div></div>
    <svg class="nav" viewBox="0 0 282 90" style="top:508px"><use href="#nav-bar"/><g color="#fff"><use href="#ic-home" x="30" y="29" width="16" height="16" opacity=".6"/><use href="#ic-search" x="99" y="29" width="16" height="16" opacity=".6"/><use href="#ic-chat" x="166" y="29" width="16" height="16"/><use href="#ic-user" x="234" y="29" width="16" height="16" opacity=".6"/></g></svg>
    <div class="homebar"></div>
  </div>

  <div class="vlabel" style="left:423px;top:2225px">VIEW MESSAGE / CHAT</div>
  <div class="screen" style="left:448px;top:2225px">
    <div class="status"><span>9:41</span><span class="sys"><i style="width:12px;height:7px"></i><i style="width:16px;height:8px"></i></span></div>
    <svg class="abs" style="left:14px;top:44px" width="16" height="16"><use href="#ic-back"/></svg>
    <span class="avatar abs" role="img" aria-label="Marisol's avatar" style="left:40px;top:38px;width:28px;height:28px"></span>
    <div class="abs" style="left:76px;top:36px"><div style="font-size:11px;font-weight:600">Marisol</div><div style="font-size:7px;color:var(--muted);display:flex;align-items:center;gap:4px"><i style="width:5px;height:5px;border-radius:50%;background:var(--green);display:block"></i>Online now</div></div>
    <svg class="abs" style="right:14px;top:44px" width="14" height="14" color="#22b573"><use href="#ic-dots"/></svg>
    <div class="abs" style="left:0;right:0;top:88px;text-align:center;font-size:7.5px;color:var(--muted)">12:13 PM</div>
    <div class="bubble out" style="top:118px">Hey there!</div>
    <span class="bubble-av" role="img" aria-label="Marisol's avatar" style="top:163px"></span>
    <div class="bubble in" style="top:164px">It's me, Hi!</div>
    <div class="bubble in" style="top:196px">I'm the problem, it's me!</div>
    <div class="bubble out" style="top:242px">Nice to meet you,</div>
    <div class="bubble out" style="top:274px">where you been?</div>
    <div class="bubble out" style="top:308px">I could show you incredible things</div>
    <span class="bubble-av" role="img" aria-label="Marisol's avatar" style="top:351px"></span>
    <div class="bubble in" style="top:352px">Oh, my God</div>
    <div class="bubble in" style="top:385px">look at that face!</div>
    <div class="bubble in" style="top:419px">You look like my next mistake</div>
    <div class="bubble out" style="top:463px">Love's a game, wanna play?</div>
    <svg class="abs" style="left:16px;top:542px" width="18" height="18"><use href="#ic-plus"/></svg>
    <div class="abs" style="left:44px;right:58px;top:538px;height:28px;border:1px solid var(--line);border-radius:8px;font-size:8px;color:#a2a7ae;display:flex;align-items:center;padding-left:10px">Reply...</div>
    <div class="abs" style="right:18px;top:538px;width:28px;height:28px;border-radius:50%;background:linear-gradient(135deg,var(--green),var(--blue));display:flex;align-items:center;justify-content:center"><svg width="12" height="12"><use href="#ic-send"/></svg></div>
    <div class="homebar dark"></div>
  </div>

  <div class="vlabel" style="left:792px;top:2225px">PROFILE SCREEN</div>
  <div class="screen" style="left:817px;top:2225px">
    <div class="status"><span>9:41</span><span class="sys"><i style="width:12px;height:7px"></i><i style="width:16px;height:8px"></i></span></div>
    <div class="pcard">
      <div class="stats"><div><b>740</b><span>FOLLOWING</span></div><div><b>506</b><span>FOLLOWERS</span></div><div><b>128</b><span>LIKES</span></div></div>
      <div class="pbtn" style="left:12px;width:112px;border:1px solid #fff;color:#fff"><svg width="9" height="9" color="#fff"><use href="#ic-edit"/></svg>Edit profile</div>
      <div class="pbtn" style="right:12px;width:112px;background:#fff;color:var(--blue)"><svg width="11" height="11" color="#1553d6"><use href="#ic-photo"/></svg>Add</div>
      <div class="abs" style="left:0;right:0;top:85px;text-align:center;color:#fff;font-size:15px;font-weight:600">Spencer</div>
    </div>
    <span class="photo photo-coast" role="img" aria-label="Profile photo of Spencer on a rocky coast" style="left:89px;top:46px;width:104px;height:104px;border-radius:50%;border:3px solid #fff"></span>
    <div class="abs" style="left:172px;top:50px;width:16px;height:16px;border-radius:4px;background:var(--blue-2);display:flex;align-items:center;justify-content:center"><svg width="10" height="10" color="#fff"><use href="#ic-photo"/></svg></div>
    <svg class="abs" style="right:20px;top:44px" width="14" height="14" color="#22b573"><use href="#ic-gear"/></svg>
    <div class="panel" style="top:306px;height:104px"><h4>Interests<svg width="10" height="10" color="#1553d6"><use href="#ic-edit"/></svg></h4>
      <div class="chips" style="margin-top:12px"><span class="chip"><i></i>Motorcycle</span><span class="chip"><i></i>Books</span><span class="chip"><i></i>Music</span><span class="chip"><i></i>Beach</span><span class="chip"><i></i>Camping</span></div></div>
    <div class="panel" style="top:429px;height:110px"><h4>More about Spencer<svg width="10" height="10" color="#1553d6"><use href="#ic-edit"/></svg></h4>
      <div class="facts"><div class="fact"><span>BIRTHDAY</span><b><svg width="9" height="9"><use href="#ic-cake"/></svg>20 Jul, 1985</b></div><div class="fact"><span>GENDER</span><b><svg width="9" height="9"><use href="#ic-male"/></svg>Male</b></div></div></div>
    <svg class="nav" viewBox="0 0 282 90" style="top:508px"><use href="#nav-bar"/><g color="#fff"><use href="#ic-home" x="30" y="29" width="16" height="16" opacity=".6"/><use href="#ic-search" x="99" y="29" width="16" height="16" opacity=".6"/><use href="#ic-chat" x="166" y="29" width="16" height="16" opacity=".6"/><use href="#ic-user" x="234" y="29" width="16" height="16"/></g></svg>
    <div class="homebar"></div>
  </div>

</div>
</body>
</html>
```